Kavoni. Sunless Tanning Mousse Label

I'm looking for a label creation for a new brand of sunless tanning solutions. They are in 6.7oz bottles (template attached).

For the front of the bottle (see template) I would like an abstract multi coloured design taking up just over half the top of the bottle (approx 60%) and going around the design (this is similar to the design inspiration attached). I would this design to use the attached colour palette of pinks. It can be swirls, drips, squares, lines, whatever you think will look good.

The logo will then be over top of that abstract design in the upper 1/3, in the colour #3fe0d0

Under the abstract design the following text:

Wild Plume (Larger text)
Coral Drift (2nd heading)
1 Hour Sunless Mousse (Sub text)
The No Orange Guarantee! (Sub text)
Vegan Formula (sub text)

The sub texts for above can be fun, have coloured background, different fonts, whatever looks good and is sill fun.

Towards the bottom of the front of bottle we require the sizing information:

200ml 6.7 Fl Oz

On the left side of the front (so in the template the middle smaller section) I would like the phrase "You ain't gotta get ready if you stay ready" Could you please make this as a separate little quote, with a fun design to it. It's like a little hidden gem on the side of the bottle.

On the back of the bottle for now can you please start towards the top with:

Wild Plume Mousse (larger)
Coral drift (second heading)
Deep Mediterranean Inspired Tan (second heading)
Easy to Apply & Streak Free
Vegan friendly & 100% natural DHA tan actives

Under this I require approx 1.5" of Lorem Ipsum for now which will take the place of directions for using the product.

Under that in small writing can we include "Warning: This product does not contain a sunscreen and will not protect against sunburn. For external use only. If skin irritation occurs, discontinue use. Carry out a patch test 24 hours prior to full body use. Store below 25(degrees sign)C."

At the bottom is the smallest yet still legible writing, can we include the ingredients that are listed below.

Target Market(s)

Females 24-35 who take care of themselves and always want to look good. It's a youthful fun product.

Requirements
Must have
• Bright colours, and just screams FUN and youthful.

Ingredients must be listed on the back. They dont' need to take up more than an inch in height, less if possible.
*******************************************

INGREDIENTS: Water (Aqua), Propylene Glycol, Dihydroxyacetone, Peg-6 Caprylic/Capric Glycerides, Dihydroxypropyl Peg-5 Linoleammonium Chloride, Peg-7 Glyceryl Cocoate, Caramel,
Phenoxyethanol, Caprylyl Glycol, Potassium Sorbate, Hexylene Glycol, Glycerin, Helianthus Annuus (Sunflower) Seed Oil, Beta Vulgaris (Beet) Root Extract, Panthenol, Solanum Lycopersicum
(Tomato) Fruit Extract, Vaccinium Macrocarpon (Cranberry) Fruit Extract, L-ascorbic Acid (Vitamin C), Tocopheryl Acetate (Vitamin E), Theobroma Cacao (Cocoa) Seed Butter, Rosa Canina (Rose Hip)
Fruit Oil, Glycine Soja (Soybean) Oil, Cucumis Sativus (Cucumber) Fruit Extract, Blue 1 (CI 42090), Red 40 (CI 16035), Yellow 6 (CI 15985), Green 5 (CI 61570), Yellow 5 (CI 19140), Red 33 (CI 17200)

*****************************
Nice to have
• Several options to choose from, some can include a gradient into geometric shapes, rather than solid colour. Experiment
Should not have
• Do not want it to look medical.
Want colours to stay in the same pink family for the abstract design - can use white also.

```html
<!DOCTYPE html>
<html lang="en">
<head>
<meta charset="utf-8">
<title>Kavoni – Wild Plume Mousse Label</title>
<link href="https://fonts.googleapis.com/css2?family=Poppins:wght@400;500;600;700;800;900&family=Yellowtail&display=swap" rel="stylesheet">
<style>
  :root {
    --pink-hot: #ff2d95;
    --pink-deep: #e0107a;
    --magenta: #c8137f;
    --lavender: #c77be0;
    --plum-text: #b01e78;
    --teal: #3fe0d0;
    --yellow: #ffe13a;
    --white: #ffffff;
    --ink: #1c1c1c;
    --page: #ffffff;
  }
  * { box-sizing: border-box; margin: 0; padding: 0; }
  html, body { width: 800px; height: 1200px; overflow: hidden; background: var(--page); }
  body { font-family: "Poppins", sans-serif; position: relative; }

  .label {
    position: absolute; left: 20px; top: 285px;
    width: 907px; height: 752px;
    transform: scale(0.838); transform-origin: 0 0;
    overflow: hidden; background: var(--white);
    box-shadow: 0 2px 10px rgba(0,0,0,0.18);
  }
  .abstract-field {
    position: absolute; inset: 0;
    background:
      radial-gradient(ellipse 260px 120px at 250px 300px, rgba(199,123,224,0.55), transparent 70%),
      radial-gradient(ellipse 200px 160px at 620px 480px, rgba(199,123,224,0.6), transparent 70%),
      radial-gradient(ellipse 240px 140px at 780px 120px, rgba(255,120,190,0.6), transparent 70%),
      radial-gradient(ellipse 220px 150px at 80px 120px, rgba(255,90,170,0.5), transparent 70%),
      linear-gradient(135deg, var(--pink-hot) 0%, var(--pink-deep) 40%, var(--magenta) 65%, var(--pink-hot) 100%);
  }
  .wave { position: absolute; inset: 0; }

  .back-panel { position: absolute; left: 40px; width: 300px; text-align: center; color: var(--white); }
  .back-title { top: 36px; font-weight: 900; font-size: 30px; line-height: 1; letter-spacing: 0.5px; }
  .back-mousse { top: 70px; font-weight: 500; font-size: 30px; line-height: 1; letter-spacing: 7px; color: var(--teal); }
  .back-base { top: 121px; font-weight: 600; font-size: 16px; letter-spacing: 4px; display: flex; align-items: center; justify-content: center; gap: 6px; }
  .back-base::before, .back-base::after { content: ""; width: 20px; height: 2px; background: var(--white); }
  .back-tan { top: 161px; font-weight: 700; font-size: 15px; line-height: 20px; color: var(--teal); }
  .back-claims { top: 221px; font-size: 13px; line-height: 15.5px; }
  .back-claims strong { font-weight: 700; }
  .back-directions { top: 293px; font-size: 13.5px; line-height: 15.5px; }

  .side-quote { position: absolute; left: 375px; top: 40px; width: 100px; height: 340px; }
  .quote-main {
    position: absolute; left: 8px; bottom: 0;
    transform: rotate(-90deg); transform-origin: 0 0;
    translate: 0 0;
    white-space: nowrap; font-weight: 600; font-size: 20px; color: var(--white); letter-spacing: 0.5px;
  }
  .quote-script {
    position: absolute; left: 40px; bottom: -12px;
    transform: rotate(-80deg); transform-origin: 0 0;
    white-space: nowrap; font-family: "Yellowtail", cursive; font-size: 42px; color: var(--yellow);
  }

  .brand-name { position: absolute; left: 508px; top: 44px; font-weight: 500; font-size: 50px; line-height: 1; color: var(--teal); display: flex; align-items: center; gap: 8px; }
  .brand-dot { width: 10px; height: 10px; background: var(--teal); border-radius: 50%; margin-top: 22px; }
  .product-name { position: absolute; left: 505px; top: 205px; font-weight: 900; font-size: 78px; line-height: 70px; color: var(--white); letter-spacing: -1px; }

  .front-lower { position: absolute; left: 505px; top: 505px; }
  .variant { font-weight: 800; font-size: 31px; color: var(--plum-text); letter-spacing: 0.5px; line-height: 1; }
  .format { margin-top: 18px; display: flex; align-items: center; gap: 6px; font-size: 16px; }
  .format-badge { background: linear-gradient(90deg, var(--pink-deep), var(--lavender)); color: var(--white); padding: 3px 5px; border-radius: 2px; }
  .format-badge b { font-weight: 700; }
  .format-type { color: var(--pink-hot); }
  .guarantee { margin-top: 24px; font-weight: 700; font-size: 14px; color: var(--pink-deep); }
  .vegan { margin-top: 20px; font-size: 13px; color: var(--teal); display: flex; align-items: center; gap: 2px; }

  .size { position: absolute; left: 752px; top: 706px; text-align: center; }
  .size-ml { font-weight: 600; font-size: 13px; color: var(--pink-deep); line-height: 1; }
  .size-oz { font-size: 8px; color: var(--ink); }

  .warning { position: absolute; left: 70px; top: 515px; width: 250px; text-align: center; color: var(--ink); font-size: 10.3px; line-height: 12px; }
  .warning-head { display: flex; align-items: center; justify-content: center; gap: 5px; color: var(--pink-deep); font-weight: 500; font-size: 9px; margin-bottom: 6px; }
  .ingredients { position: absolute; left: 62px; top: 618px; width: 268px; text-align: center; font-size: 6.4px; line-height: 8px; color: var(--ink); }
  .ingredients b { font-weight: 700; }
</style>
</head>
<body>
  <div class="label">
    <div class="abstract-field" role="img" aria-label="Abstract marbled swirl pattern in hot pink, magenta and lavender"></div>

    <svg class="wave" viewBox="0 0 907 752" width="907" height="752" aria-hidden="true">
      <path fill="#ffffff" d="M0,412 C50,400 100,440 170,425 C230,412 260,385 300,390 C350,395 370,420 390,440 C410,470 420,530 440,535 C470,540 490,470 520,440 C550,410 600,395 650,400 C700,405 730,440 770,455 C810,470 850,400 907,405 L907,752 L0,752 Z"/>
      <circle cx="320" cy="413" r="20" fill="#ff2d95"/>
      <circle cx="570" cy="425" r="20" fill="#e0107a"/>
      <circle cx="697" cy="408" r="12" fill="#ffffff"/>
      <circle cx="873" cy="432" r="12" fill="#e0107a"/>
    </svg>

    <div class="back-panel back-title">WILD PLUME</div>
    <div class="back-panel back-mousse">MOUSSE</div>
    <div class="back-panel back-base">CORAL DRIFT</div>
    <div class="back-panel back-tan">DEEP MEDITERRANEAN<br>INSPIRED TAN</div>
    <div class="back-panel back-claims"><strong>Easy to Apply &amp; Streak Free</strong><br>Vegan friendly &amp; 100% natural<br>DHA tan actives</div>
    <div class="back-panel back-directions">Lorem ipsum dolor sit amet,<br>consectetuer adipiscing elit, sed diam<br>nonummy nibh euismod tincidunt ut<br>laoreet dolore magna.</div>

    <div class="side-quote">
      <div class="quote-main">YOU AIN'T GOTTA GET READY</div>
      <div class="quote-script">if you stay ready</div>
    </div>

    <div class="brand-name">Kavoni<span class="brand-dot"></span></div>
    <div class="product-name">WILD<br>PLUME</div>

    <div class="front-lower">
      <div class="variant">CORAL DRIFT</div>
      <div class="format"><span class="format-badge"><b>1 Hour</b> Sunless</span><span class="format-type">Mousse</span></div>
      <div class="guarantee">THE NO ORANGE GUARANTEE!</div>
      <div class="vegan">
        <svg width="12" height="12" viewBox="0 0 12 12" aria-hidden="true"><path d="M1,11 C1,4 5,1 11,1 C11,7 7,11 1,11 Z" fill="#3fe0d0"/></svg>
        Vegan Formula
      </div>
    </div>

    <div class="size"><div class="size-ml">200ml</div><div class="size-oz">6.7 Fl Oz</div></div>

    <div class="warning">
      <div class="warning-head">
        <svg width="14" height="12" viewBox="0 0 14 12" aria-hidden="true"><path d="M7,1 L13,11 L1,11 Z" fill="none" stroke="#e0107a" stroke-width="1.2"/><path d="M7,4.5 V8" stroke="#e0107a" stroke-width="1.2"/><circle cx="7" cy="9.4" r="0.7" fill="#e0107a"/></svg>
        WARNING
      </div>
      This product does not contain a sunscreen and will not protect against sunburn. For external use only. If skin irritation occurs, discontinue use. Carry out a patch test 24 hours prior to full body use. Store below 25ºC.
    </div>

    <div class="ingredients"><b>INGREDIENTS:</b> Water (Aqua), Propylene Glycol, Dihydroxyacetone, Peg-6 Caprylic/Capric Glycerides, Dihydroxypropyl Peg-5 Linoleammonium Chloride, Peg-7 Glyceryl Cocoate, Caramel, Phenoxyethanol, Caprylyl Glycol, Potassium Sorbate, Hexylene Glycol, Glycerin, Helianthus Annuus (Sunflower) Seed Oil, Beta Vulgaris (Beet) Root Extract, Panthenol, Solanum Lycopersicum (Tomato) Fruit Extract, Vaccinium Macrocarpon (Cranberry) Fruit Extract, L-ascorbic Acid (Vitamin C), Tocopheryl Acetate (Vitamin E), Theobroma Cacao (Cocoa) Seed Butter, Rosa Canina (Rose Hip) Fruit Oil, Glycine Soja (Soybean) Oil, Cucumis Sativus (Cucumber) Fruit Extract, Blue 1 (CI 42090), Red 40 (CI 16035), Yellow 6 (CI 15985), Green 5 (CI 61570), Yellow 5 (CI 19140), Red 33 (CI 17200)</div>
  </div>
</body>
</html>
```